Lanternfold Cybersecurity Web Site Project

Lanternfold Cybersecurity is an MSP provider that is a full-service IT delivery organization focused on service deliver and information security.

We are looking for CREATIVE and UNIQUE website design that lays out the initial landing page and content page for us to continue developing for our organization. We have attached a .zip of our logo and images stock for you to incorporate into the site.

We are a Cybersecurity / MSP focused on providing a full-service outsourced IT Services to organizations that also have information cybersecurity compliance requirements such as HIPAA, PCI-DSS,
NYS DFS 23 NYCRR 500.

Systems / Applications Solutions:
On-Premises and Cloud Solutions
IT Services / Help Desk
User and System Issue Resolution
CloudOffice Administration
Nimbus / Cloud Virtualization
Windows / Linux Server Administration

We are looking for two (2) .psd design files for the landing page and content page based on the logo stock art provided and all files / artwork created by the designer at project completion.

Please be creative and make this site stand out from all others. We are well aware of template sites like Pixel Orchard and others like it, so please we are not looking for a template we could download ourselves.

Target Market(s)

Demographic: Law Firms, Legal Services, Small - Medium Doctor offices, Medical services companies, Finance, Mortgage, Securities.

Businesses looking to outsource their IT departments.
Move to a full cloud business solution.
Require cybersecurity compliance such as HIPAA, PCI-DSS or DFS 23 NYCRR 500.

Industry/Entity Type

Information Technology

Number of Pages Required

2 page

Requirements
Must have
• We have included stock art for logo's, banners, headers, footers, please use that graphic stock for the site.

We operate in the Managed Service Provider (MSP) and Cybersecurity space
Should not have
• Themes we can get from any of the theme sites out there. We are looking for something completely new and unique.

```html
<!DOCTYPE html>
<html lang="en">
<head>
<meta charset="utf-8">
<title>Lanternfold Cybersecurity</title>
<link href="https://fonts.googleapis.com/css2?family=Roboto:wght@400;500;700;900&family=Poppins:wght@700;800&display=swap" rel="stylesheet">
<style>
:root{
  --red:#b0141c;
  --red-dark:#8e0f16;
  --navy:#0d1630;
  --navy-deep:#081027;
  --ink:#1b1b1f;
  --text:#3d3d42;
  --muted:#6a6a70;
  --paper:#ffffff;
  --mist:#f2f0f0;
  --card:#e5e4e4;
  --panel:#e4e3e4;
  --divider:#c9c9cc;
  --footer:#17171b;
}
*{box-sizing:border-box;margin:0;padding:0}
html,body{width:1200px;height:3951px;overflow:hidden}
body{position:relative;background:var(--paper);font-family:"Roboto",Arial,sans-serif;color:var(--text)}
.abs{position:absolute}
.btn{position:absolute;display:flex;align-items:center;justify-content:center;background:var(--red);color:#fff;font-weight:700;text-transform:uppercase;font-family:"Roboto",Arial,sans-serif}
.btn-sm{width:78px;height:24px;font-size:9px}
.rule{position:absolute;height:3px;background:var(--red)}
.section-title{position:absolute;left:0;width:1200px;text-align:center;font-weight:700;font-size:22px;color:var(--ink);text-transform:uppercase}

/* header */
.brand{position:absolute;left:133px;top:30px;display:flex;align-items:center;gap:12px}
.brand-mark{width:40px;height:40px;border-radius:50%;background:var(--red)}
.brand-name{font-size:26px;font-weight:700;color:var(--ink);line-height:1}
.follow{position:absolute;left:730px;top:33px;display:flex;align-items:center;gap:8px;font-size:11px;color:var(--ink);font-weight:500}
.social-dot{width:24px;height:24px;border-radius:50%;background:#26365f}
.call{position:absolute;left:875px;top:20px;display:flex;gap:10px;align-items:flex-start}
.call small{display:block;font-size:11px;color:var(--ink)}
.call strong{display:block;font-size:23px;color:var(--red);font-weight:700;line-height:1.1}
.nav{position:absolute;right:130px;top:76px;display:flex;gap:35px;font-size:13px;font-weight:700;color:var(--ink)}
.nav .active{color:var(--red);border-bottom:2px solid var(--red)}

/* hero */
.hero{position:absolute;left:0;top:113px;width:1200px;height:544px;background:linear-gradient(180deg,#b6c8d0 0%,#6f94a8 35%,#2c6780 65%,#183e55 100%)}
.hero-title{position:absolute;left:0;top:190px;width:1200px;text-align:center;font-family:"Poppins",Arial,sans-serif;font-weight:800;font-size:43px;color:#fff;text-transform:uppercase;text-shadow:0 2px 6px rgba(0,0,0,.35)}
.hero .btn{left:533px;top:269px;width:135px;height:39px;font-size:16px}
.arrow{position:absolute;top:255px;width:34px;height:34px;background:#fff;display:flex;align-items:center;justify-content:center}

/* welcome */
.welcome-mark{position:absolute;left:175px;top:712px;width:310px;height:318px;border-radius:50%;background:radial-gradient(circle at 40% 40%,#d1202a,#6e0a10);display:flex;align-items:center;justify-content:center}
.welcome-mark span{color:#fff;font-size:26px;font-weight:700}
.welcome-kicker{position:absolute;left:535px;top:703px;font-size:22px;color:var(--ink)}
.welcome-title{position:absolute;left:535px;top:733px;font-size:34px;font-weight:700;color:var(--ink)}
.welcome-copy{position:absolute;left:537px;top:829px;width:510px;font-size:14px;line-height:21px;color:var(--text)}

/* solutions */
.solutions{position:absolute;left:0;top:1080px;width:1200px;height:700px;background:var(--mist)}
.card{position:absolute;width:275px;height:268px;background:var(--card);text-align:center}
.card svg{position:absolute;left:112px;top:30px}
.card h3{position:absolute;left:0;top:105px;width:100%;font-size:13px;font-weight:700;color:var(--ink);line-height:19px;text-transform:uppercase}
.card p{position:absolute;left:35px;top:158px;width:205px;font-size:11.5px;line-height:16px;color:var(--muted)}
.card .btn{left:98px;top:217px}
.card-feature{background:radial-gradient(circle at 60% 40%,#2d6fb5,#0b2f6b 55%,#06163a)}
.card-feature .outline{position:absolute;left:49px;top:106px;width:177px;height:39px;border:2px solid #fff;color:#fff;font-size:13px;font-weight:500;display:flex;align-items:center;justify-content:center;letter-spacing:.3px}

/* compliance */
.compliance{position:absolute;left:0;top:1720px;width:1200px;height:663px}
.comp-col{position:absolute;width:280px;text-align:center;color:#fff}
.badge{margin:0 auto;background:#fff}
.comp-col h3{position:absolute;top:150px;width:100%;font-size:17px;font-weight:700}
.comp-col p{position:absolute;top:180px;left:18px;width:244px;font-size:12px;line-height:16px;color:#b8bccb}

/* targets */
.targets-title{position:absolute;left:130px;top:2540px;font-size:22px;font-weight:700;color:var(--ink)}
.targets-copy{position:absolute;left:131px;top:2623px;width:300px;font-size:13.5px;line-height:18px;color:var(--text)}
.target-panel{position:absolute;left:484px;top:2420px;width:585px;height:500px;background:var(--panel);border-radius:0 0 120px 120px}
.target-grid{position:absolute;left:0;top:0}
.target{position:absolute;width:165px;text-align:center;font-size:12.5px;font-weight:500;color:var(--ink);text-transform:uppercase;line-height:16px}
.target svg{display:block;margin:0 auto 14px}

/* blog */
.blog{position:absolute;left:0;top:2980px;width:1200px;height:580px;background:#ececec}
.post{position:absolute;top:3118px;width:285px}
.post-img{width:285px;height:167px}
.post h3{margin-top:25px;width:255px;font-size:13.5px;font-weight:700;color:var(--ink);line-height:19px;text-transform:uppercase}
.post p{margin-top:12px;font-size:11.5px;line-height:15px;color:var(--muted);width:270px}
.post .btn{position:relative;margin-top:10px;width:74px}

/* footer */
.footer{position:absolute;left:0;top:3430px;width:1200px;height:521px}
.foot-mark{position:absolute;left:133px;top:3592px;width:190px;height:190px;border-radius:50%;background:radial-gradient(circle at 40% 40%,#c81a24,#5a080d);display:flex;align-items:center;justify-content:center;color:#fff;font-size:16px;font-weight:700;text-align:center}
.foot-head{position:absolute;top:3614px;font-size:14px;font-weight:700;color:#fff;text-transform:uppercase}
.foot-menu{position:absolute;left:441px;top:3655px;font-size:12.5px;line-height:22px;color:#d9d9de;list-style:none;text-transform:uppercase}
.foot-item{position:absolute;display:flex;gap:12px;font-size:12.5px;line-height:17px;color:#d9d9de}
.foot-icon{width:24px;height:24px;border-radius:50%;background:var(--red);flex:none;display:flex;align-items:center;justify-content:center}
.foot-line{position:absolute;left:130px;top:3885px;width:940px;height:1px;background:#33333a}
.copyright{position:absolute;left:0;top:3910px;width:1200px;text-align:center;font-size:10.5px;color:#b7b7bd}
</style>
</head>
<body>

<!-- header -->
<div class="brand"><span class="brand-mark"></span><span class="brand-name">Lanternfold Cybersecurity</span></div>
<div class="follow">FOLLOW <span class="social-dot"></span><span class="social-dot"></span></div>
<div class="call">
  <svg width="26" height="26" viewBox="0 0 24 24" fill="none" stroke="#1b1b1f" stroke-width="1.6"><path d="M5 3h4l2 5-2.5 1.5a11 11 0 0 0 6 6L16 13l5 2v4a2 2 0 0 1-2 2A16 16 0 0 1 3 5a2 2 0 0 1 2-2z"/></svg>
  <div><small>CALL US AT</small><strong>800.555.0142</strong></div>
</div>
<nav class="nav"><span class="active">HOME</span><span>ABOUT US</span><span>SERVICES</span><span>BLOG</span><span>CONTACT US</span></nav>

<!-- hero -->
<section class="hero" role="img" aria-label="City skyline at dusk with a glowing digital cloud above it">
  <h1 class="hero-title">Cloud Business Solution</h1>
  <span class="btn">Read More</span>
  <span class="arrow" style="left:0"><svg width="14" height="14" viewBox="0 0 14 14"><path d="M9 2 4 7l5 5" stroke="#2a6fb0" stroke-width="2" fill="none"/></svg></span>
  <span class="arrow" style="right:0"><svg width="14" height="14" viewBox="0 0 14 14"><path d="M5 2l5 5-5 5" stroke="#2a6fb0" stroke-width="2" fill="none"/></svg></span>
</section>

<!-- welcome -->
<div class="welcome-mark"><span>Lanternfold</span></div>
<div class="welcome-kicker">Welcome to</div>
<h2 class="welcome-title">Lanternfold Cybersecurity</h2>
<div class="rule" style="left:535px;top:787px;width:103px"></div>
<p class="welcome-copy">At vero eos et accusamus et iusto odio dignissimos ducimus qui blanditiis praesentium voluptatum deleniti atque corrupti quos dolores et quas molestias excepturi sint occaecati cupiditate non provident, similique sunt in culpa qui officia deserunt mollitia animi, id est laborum et dolorum fuga. Et harum quidem rerum facilis est et expedita distinctio.</p>
<span class="btn" style="left:540px;top:977px;width:102px;height:31px;font-size:12px">Read More</span>

<!-- solutions -->
<section class="solutions"></section>
<h2 class="section-title" style="top:1122px">Our Solutions</h2>
<div class="rule" style="left:574px;top:1160px;width:52px"></div>

<div class="card" style="left:178px;top:1205px">
  <svg width="52" height="52" viewBox="0 0 52 52" fill="#b0141c"><path d="M14 30a9 9 0 0 1 2-17 12 12 0 0 1 22 3 7 7 0 0 1 0 14z"/><path d="M18 30v10M26 30v14M34 30v10" stroke="#b0141c" stroke-width="2"/><circle cx="18" cy="42" r="3"/><circle cx="26" cy="46" r="3"/><circle cx="34" cy="42" r="3"/></svg>
  <h3>On-Premises and<br>Cloud Solutions</h3>
  <p>At vero eos et accusamus et iusto odio dignissimos ducimus qui blanditiis praesentium.</p>
  <span class="btn btn-sm">Read More</span>
</div>
<div class="card" style="left:462px;top:1205px">
  <svg width="52" height="52" viewBox="0 0 52 52" fill="#b0141c"><circle cx="26" cy="16" r="9"/><path d="M8 50a18 16 0 0 1 36 0z"/><path d="M15 16a11 11 0 0 1 22 0" stroke="#1b1b1f" stroke-width="2.5" fill="none"/></svg>
  <h3>IT Services /<br>Help Desk</h3>
  <p>At vero eos et accusamus et iusto odio dignissimos ducimus qui blanditiis praesentium.</p>
  <span class="btn btn-sm">Read More</span>
</div>
<div class="card" style="left:744px;top:1205px">
  <svg width="52" height="52" viewBox="0 0 52 52"><path d="M10 4h24l10 10v34H10z" fill="#b0141c"/><circle cx="27" cy="30" r="8" fill="none" stroke="#fff" stroke-width="4"/></svg>
  <h3>User and System<br>Issue Resolution</h3>
  <p>At vero eos et accusamus et iusto odio dignissimos ducimus qui blanditiis praesentium.</p>
  <span class="btn btn-sm">Read More</span>
</div>
<div class="card" style="left:178px;top:1482px">
  <svg width="52" height="52" viewBox="0 0 52 52"><rect x="12" y="8" width="28" height="36" fill="#b0141c"/></svg>
  <h3>CloudOffice<br>Administration</h3>
  <p>At vero eos et accusamus et iusto odio dignissimos ducimus qui blanditiis praesentium.</p>
  <span class="btn btn-sm">Read More</span>
</div>
<div class="card" style="left:462px;top:1482px">
  <svg width="52" height="52" viewBox="0 0 52 52" fill="#b0141c"><path d="M12 34a10 10 0 0 1 3-19 13 13 0 0 1 24 3 8 8 0 0 1 0 16z"/><circle cx="26" cy="34" r="9" fill="#e5e4e4"/><circle cx="26" cy="34" r="6" fill="none" stroke="#b0141c" stroke-width="3"/></svg>
  <h3>Nimbus / Cloud<br>Virtualization</h3>
  <p>At vero eos et accusamus et iusto odio dignissimos ducimus qui blanditiis praesentium.</p>
  <span class="btn btn-sm">Read More</span>
</div>
<div class="card card-feature" style="left:744px;top:1482px" role="img" aria-label="Glowing blue network of connected nodes">
  <span class="outline">VIEW ALL SOLUTIONS</span>
</div>

<!-- compliance -->
<svg class="compliance" width="1200" height="663" viewBox="0 0 1200 663" preserveAspectRatio="none">
  <path d="M0 10 Q600 190 1200 10 V663 H0 Z" fill="#0b1330"/>
  <path d="M0 0 Q600 180 1200 0 V10 Q600 190 0 10 Z" fill="#b0141c"/>
</svg>
<h2 class="section-title" style="top:1905px;color:#fff">Cybersecurity Compliance</h2>
<div class="rule" style="left:574px;top:1953px;width:52px"></div>

<div class="comp-col" style="left:123px;top:2000px">
  <div class="badge" style="width:100px;height:100px;border-radius:50%"></div>
  <h3>HIPAA</h3>
  <p>On the other hand, we denounce with righteous indignation and dislike men who are so beguiled and demoralized by the charms of pleasure. desire, that they cannot foresee the pain</p>
</div>
<div class="comp-col" style="left:460px;top:2000px">
  <div class="badge" style="width:190px;height:70px;margin-top:15px;border-radius:4px"></div>
  <h3>PCI-DSS</h3>
  <p>On the other hand, we denounce with righteous indignation and dislike men who are so beguiled and demoralized by the charms of pleasure. desire, that they cannot foresee the pain</p>
</div>
<div class="comp-col" style="left:802px;top:2000px">
  <div class="badge" style="width:176px;height:56px;margin-top:32px;border-radius:6px"></div>
  <h3>DFS 23 NYCRR 500</h3>
  <p>On the other hand, we denounce with righteous indignation and dislike men who are so beguiled and demoralized by the charms of pleasure. desire, that they cannot foresee the pain</p>
</div>
<span class="btn btn-sm" style="left:223px;top:2289px">Read More</span>
<span class="btn btn-sm" style="left:566px;top:2289px">Read More</span>
<span class="btn btn-sm" style="left:913px;top:2289px">Read More</span>

<!-- targets -->
<h2 class="targets-title">OUR TARGETS ARE</h2>
<div class="rule" style="left:131px;top:2584px;width:50px"></div>
<p class="targets-copy">At vero eos et accusamus et iusto odio dignis simos ducimus qui blanditiis praesentium voluptatum deleniti atque corrupti quos dolores et quas molestias excepturi sint occaecati cupiditate non provident, similique sunt in culpa qui officia deserunt mollitia animi, id est laborum et dolorum fuga. Et harum quidem rerum facilis est et expedita distinctio.</p>
<span class="btn" style="left:133px;top:2803px;width:104px;height:31px;font-size:12px">Read More</span>

<div class="target-panel" role="img" aria-label="Light grey backdrop panel behind the target markets">
  <svg class="target-grid" width="585" height="500" viewBox="0 0 585 500">
    <line x1="225" y1="118" x2="225" y2="390" stroke="#c9c9cc"/>
    <line x1="392" y1="118" x2="392" y2="390" stroke="#c9c9cc"/>
    <line x1="90" y1="240" x2="520" y2="240" stroke="#c9c9cc"/>
  </svg>
</div>
<div class="target" style="left:546px;top:2548px"><svg width="44" height="44" viewBox="0 0 44 44" fill="#1b2a4a"><path d="M4 14 22 4l18 10z"/><rect x="8" y="17" width="4" height="18"/><rect x="17" y="17" width="4" height="18"/><rect x="26" y="17" width="4" height="18"/><rect x="34" y="17" width="4" height="18"/><rect x="4" y="37" width="36" height="4"/></svg>Law Firms</div>
<div class="target" style="left:712px;top:2548px"><svg width="44" height="44" viewBox="0 0 44 44" fill="#1b2a4a"><rect x="10" y="4" width="26" height="36"/><rect x="15" y="12" width="16" height="3" fill="#fff"/><rect x="15" y="19" width="16" height="3" fill="#fff"/><rect x="15" y="26" width="10" height="3" fill="#fff"/></svg>Securities</div>
<div class="target" style="left:854px;top:2548px"><svg width="44" height="44" viewBox="0 0 44 44" fill="none" stroke="#1b2a4a" stroke-width="3"><path d="M6 18 22 10l16 8-16 8z"/><path d="M6 25l16 8 16-8"/><path d="M6 32l16 8 16-8"/></svg>Finance</div>
<div class="target" style="left:546px;top:2683px"><svg width="44" height="44" viewBox="0 0 44 44" fill="#1b2a4a"><rect x="6" y="10" width="32" height="32"/><rect x="18" y="2" width="8" height="10"/><rect x="11" y="16" width="5" height="5" fill="#fff"/><rect x="28" y="16" width="5" height="5" fill="#fff"/><rect x="18" y="30" width="8" height="12" fill="#fff"/></svg>Medium Doctor<br>Offices</div>
<div class="target" style="left:712px;top:2683px"><svg width="44" height="44" viewBox="0 0 44 44" fill="#1b2a4a"><rect x="18" y="2" width="8" height="40"/><rect x="18" y="2" width="8" height="40" transform="rotate(60 22 22)"/><rect x="18" y="2" width="8" height="40" transform="rotate(-60 22 22)"/></svg>Medical Services<br>Companies</div>
<div class="target" style="left:854px;top:2683px"><svg width="44" height="44" viewBox="0 0 44 44" fill="#1b2a4a"><path d="M4 24 22 8l18 16h-6v16H10V24z"/><circle cx="22" cy="16" r="7" fill="#e4e3e4"/><circle cx="22" cy="16" r="5"/></svg>Mortgage</div>

<!-- blog -->
<section class="blog"></section>
<h2 class="section-title" style="top:3027px">Latest Blog</h2>
<div class="rule" style="left:583px;top:3066px;width:52px"></div>
<article class="post" style="left:140px">
  <div class="post-img" role="img" aria-label="Hand touching a glowing security shield interface" style="background:linear-gradient(135deg,#1e3a6b,#6d8fc0 50%,#223f6e)"></div>
  <h3>On the other hand we enounce with righte</h3>
  <p>At vero eos et accusamus et iusto odio dignis simos ducimus qui blanditiis praesentium voluptatum deleniti atque</p>
  <span class="btn btn-sm">Read More</span>
</article>
<article class="post" style="left:463px">
  <div class="post-img" role="img" aria-label="Laptop with a glowing cloud computing hologram" style="background:linear-gradient(135deg,#0e2a4e,#3f7fb0 50%,#0b1d38)"></div>
  <h3>On the other hand we enounce with righte</h3>
  <p>At vero eos et accusamus et iusto odio dignis simos ducimus qui blanditiis praesentium voluptatum deleniti atque</p>
  <span class="btn btn-sm">Read More</span>
</article>
<article class="post" style="left:792px">
  <div class="post-img" role="img" aria-label="Cloud shape on a blue circuit board" style="background:linear-gradient(135deg,#0f3e78,#3a7cc7 55%,#0a2b5a)"></div>
  <h3>On the other hand we enounce with righte</h3>
  <p>At vero eos et accusamus et iusto odio dignis simos ducimus qui blanditiis praesentium voluptatum deleniti atque</p>
  <span class="btn btn-sm">Read More</span>
</article>

<!-- footer -->
<svg class="footer" width="1200" height="521" viewBox="0 0 1200 521" preserveAspectRatio="none">
  <path d="M0 12 Q600 200 1200 12 V521 H0 Z" fill="#17171b"/>
  <path d="M0 0 Q600 190 1200 0 V12 Q600 200 0 12 Z" fill="#b0141c"/>
</svg>
<div class="foot-mark">Lanternfold<br>Cybersecurity</div>
<div class="foot-head" style="left:441px">Menu</div>
<ul class="foot-menu"><li>Home</li><li>About Us</li><li>Services</li><li>Blog</li><li>Contact Us</li></ul>
<div class="foot-head" style="left:636px">Contact Us</div>
<div class="foot-item" style="left:634px;top:3658px"><span class="foot-icon"><svg width="10" height="12" viewBox="0 0 10 12"><path d="M5 0a4 4 0 0 1 4 4c0 3-4 8-4 8S1 7 1 4a4 4 0 0 1 4-4z" fill="#fff"/></svg></span><span>2207 Harbor Lantern Road<br>Brightwater, CA 90000</span></div>
<div class="foot-item" style="left:634px;top:3716px"><span class="foot-icon"><svg width="12" height="12" viewBox="0 0 24 24"><path d="M5 3h4l2 5-2.5 1.5a11 11 0 0 0 6 6L16 13l5 2v4a2 2 0 0 1-2 2A16 16 0 0 1 3 5a2 2 0 0 1 2-2z" fill="#fff"/></svg></span><span>Call Us<br>800.555.0142</span></div>
<div class="foot-item" style="left:634px;top:3773px"><span class="foot-icon"><svg width="12" height="9" viewBox="0 0 12 9"><rect width="12" height="9" fill="#fff"/><path d="M0 0l6 5 6-5" stroke="#b0141c" fill="none"/></svg></span><span>E mail Us<br>info@lanternfoldcyber.com</span></div>
<div class="foot-head" style="left:951px">Follow Us</div>
<div class="foot-item" style="left:949px;top:3658px"><span class="foot-icon"></span><span>Like us on<br>CHATTERBOOK</span></div>
<div class="foot-item" style="left:949px;top:3716px"><span class="foot-icon"></span><span>Follow us on<br>CHIRPER</span></div>
<div class="foot-item" style="left:949px;top:3773px"><span class="foot-icon"></span><span>Follow us on<br>WORKLINK</span></div>
<div class="foot-line"></div>
<p class="copyright">Copyright © 2020 All Rights Reserved</p>

</body>
</html>
```